Business Card Design

we are a brand new cable TV network devoted to self improvement and leading a better life called FLOURISH TV.I have a logo. We have 3 executives that need cards.I want it to be a heavy stock card: professional but showing our creative nature

Industry/Entity Type

Business

Contact Information for Business Card

CLAUDIA SAENZ AMLIECEO350 San Juan DrPonte Vedra Beach FL 32082904-473-5953

```html
<!DOCTYPE html>
<html lang="en">
<head>
<meta charset="utf-8">
<title>Flourish TV — Business Cards</title>
<link href="https://fonts.googleapis.com/css2?family=Lato:wght@400;700&display=swap" rel="stylesheet">
<style>
  :root {
    --backdrop: #4a2c1c;
    --card: #ffffff;
    --ink: #231f20;
    --brand-red: #d3222a;
    --rule: #1f1c1d;
  }
  * { box-sizing: border-box; margin: 0; padding: 0; }
  html, body {
    width: 1200px; height: 978px; overflow: hidden;
    background: var(--backdrop);
    font-family: 'Lato', sans-serif;
    color: var(--ink);
  }
  .canvas { position: relative; width: 1200px; height: 978px; }
  .card {
    position: absolute;
    width: 706px; height: 404px;
    background: var(--card);
    border-radius: 8px;
    overflow: hidden;
    box-shadow: 0 4px 12px rgba(0,0,0,0.35);
  }
  .card--front { left: 230px; top: 54px; }
  .card--back  { left: 228px; top: 497px; height: 402px; }

  .wordmark {
    position: absolute; left: 0; width: 100%;
    display: flex; align-items: center; justify-content: center; gap: 18px;
    font-weight: 700; font-size: 84px; line-height: 1;
    color: var(--ink); letter-spacing: -1px;
  }
  .card--front .wordmark { top: 54px; }
  .card--back .wordmark  { top: 164px; }
  .wordmark__dot {
    width: 62px; height: 62px; border-radius: 50%;
    background: var(--brand-red); flex: none;
  }

  .holder {
    position: absolute; top: 230px; left: 0; width: 100%;
    text-align: center;
  }
  .holder__name { font-weight: 700; font-size: 23px; letter-spacing: 0.2px; }
  .holder__title { font-weight: 700; font-size: 23px; color: var(--brand-red); margin-top: 6px; letter-spacing: 1px; }

  .divider {
    position: absolute; left: 47px; top: 294px;
    width: 614px; height: 1.5px; background: var(--rule);
  }

  .contact {
    position: absolute; top: 316px; left: 0; width: 100%; height: 46px;
    font-size: 20px;
  }
  .contact__phone {
    position: absolute; right: 352px; top: 12px;
    display: flex; align-items: center; gap: 12px; white-space: nowrap;
  }
  .contact__phone svg { width: 20px; height: 18px; }
  .contact__sep {
    position: absolute; left: 353px; top: 0; width: 1px; height: 44px;
    background: var(--rule);
  }
  .contact__address {
    position: absolute; left: 369px; top: 0; line-height: 24px; white-space: nowrap;
  }

  .base-band { position: absolute; left: 0; bottom: 0; width: 100%; height: 30px; }
</style>
</head>
<body>
<div class="canvas">

  <section class="card card--front">
    <div class="wordmark"><span class="wordmark__dot"></span><span>Flourish TV</span></div>

    <div class="holder">
      <p class="holder__name">MARISOL DUVAL KERNO</p>
      <p class="holder__title">CEO</p>
    </div>

    <div class="divider"></div>

    <div class="contact">
      <div class="contact__phone">
        <span>555-218-0476</span>
        <svg viewBox="0 0 20 18" aria-hidden="true">
          <path fill="#d3222a" d="M2 6 C2 2 18 2 18 6 L18 8 L14 8 L13.5 6 L6.5 6 L6 8 L2 8 Z M5 9 L15 9 L17 16 L3 16 Z"/>
          <circle cx="10" cy="12.3" r="2" fill="#fff"/>
        </svg>
      </div>
      <div class="contact__sep"></div>
      <div class="contact__address">
        <p>718 Copper Hollow Ln</p>
        <p>Harbor Glen FL 30915</p>
      </div>
    </div>

    <svg class="base-band" viewBox="0 0 706 30" preserveAspectRatio="none" aria-hidden="true">
      <rect x="0" y="8" width="706" height="10" fill="#d3222a"/>
      <rect x="0" y="18" width="706" height="12" fill="#231f20"/>
      <polygon points="226,0 484,0 500,18 210,18" fill="#231f20"/>
    </svg>
  </section>

  <section class="card card--back">
    <div class="wordmark"><span class="wordmark__dot"></span><span>Flourish TV</span></div>

    <svg class="base-band" viewBox="0 0 706 30" preserveAspectRatio="none" aria-hidden="true">
      <rect x="0" y="8" width="706" height="10" fill="#d3222a"/>
      <rect x="0" y="18" width="706" height="12" fill="#231f20"/>
      <polygon points="228,0 484,0 500,18 212,18" fill="#231f20"/>
    </svg>
  </section>

</div>
</body>
</html>
```